Life Coach for Lawyers Business Card Design

Elegant, original, business card design for life coaching service for associate attorneys who work in big law and struggle with stress, overwhelm, and time management. Double sided design.

Target Market(s)

Women associate attorneys who work in big law and struggle with stress, overwhelm, and time management.

Industry/Entity Type

Life Coaching

Contact Information for Business Card

Marissa Pendrell
Life Coach
518.677.3941
calmbriefcounsel.net
marissa@calmbriefcounsel.net
@calmbriefcounsel (Instagram)

Font styles to use
Other font styles liked:
• Silver South font duo. See uploaded files.

Requirements
Must have
• Icons for phone, website, email, and Instagram instead of words. Specific colors used in my logo (171B2B, 421121, FFFFFF)
Nice to have
• Foil. Embossed. Feminine design.
Should not have
• Any colors other than those used in logo. See uploaded files.

```html
<!DOCTYPE html>
<html lang="en">
<head>
<meta charset="utf-8">
<title>Calm Brief Counsel – Business Card</title>
<link rel="stylesheet" href="https://fonts.googleapis.com/css2?family=Playfair+Display:wght@400;500&family=Mrs+Saint+Delafield&family=Jost:wght@300;400&display=swap">
<style>
  :root {
    --navy: #171B2B;
    --plum: #421121;
    --white: #FFFFFF;
    --edge: #000000;
  }
  * { margin: 0; padding: 0; box-sizing: border-box; }
  html, body {
    width: 934px;
    height: 1200px;
    overflow: hidden;
    background: var(--white);
  }
  .sheet {
    position: relative;
    width: 934px;
    height: 1200px;
  }
  .card {
    position: absolute;
    left: 0;
    width: 934px;
    height: 534px;
    border: 1px solid var(--edge);
    background: var(--white);
  }
  .card--front { top: 0; }
  .card--back { top: 666px; }

  .brand {
    position: absolute;
    left: 0;
    right: 0;
    top: 226px;
    text-align: center;
    font-family: "Playfair Display", serif;
    font-weight: 400;
    font-size: 70px;
    letter-spacing: 0.02em;
    color: var(--plum);
    line-height: 1;
    white-space: nowrap;
  }

  .holder-name {
    position: absolute;
    left: 147px;
    top: 58px;
    font-family: "Mrs Saint Delafield", cursive;
    font-weight: 400;
    font-size: 96px;
    line-height: 1.2;
    color: var(--plum);
    white-space: nowrap;
  }
  .holder-role {
    position: absolute;
    left: 145px;
    top: 211px;
    font-family: "Playfair Display", serif;
    font-weight: 500;
    font-size: 24px;
    letter-spacing: 0.42em;
    color: var(--navy);
    line-height: 1;
    white-space: nowrap;
  }

  .contact-list {
    position: absolute;
    left: 133px;
    top: 280px;
    list-style: none;
  }
  .contact-item {
    position: absolute;
    left: 0;
    display: flex;
    align-items: center;
    height: 38px;
    white-space: nowrap;
  }
  .contact-item:nth-child(1) { top: 0; }
  .contact-item:nth-child(2) { top: 52px; }
  .contact-item:nth-child(3) { top: 104px; }
  .contact-item:nth-child(4) { top: 156px; }
  .contact-icon {
    width: 37px;
    height: 37px;
    flex: none;
  }
  .contact-text {
    margin-left: 14px;
    font-family: "Jost", sans-serif;
    font-weight: 400;
    font-size: 28px;
    letter-spacing: 0.2em;
    color: var(--navy);
  }
</style>
</head>
<body>
<main class="sheet">

  <section class="card card--front" aria-label="Card front">
    <p class="brand">Calm Brief Counsel</p>
  </section>

  <section class="card card--back" aria-label="Card back">
    <h1 class="holder-name">Marissa Pendrell</h1>
    <p class="holder-role">-LIFE COACH-</p>

    <ul class="contact-list">
      <li class="contact-item">
        <svg class="contact-icon" viewBox="0 0 40 40" aria-hidden="true">
          <circle cx="20" cy="20" r="20" fill="var(--plum)"/>
          <path d="M13 10.5c1-.8 2.2-.6 2.8.4l2 3.3c.5.9.3 1.8-.4 2.4l-1.4 1.1c.9 2.4 2.7 4.4 5 5.6l1.2-1.3c.7-.7 1.7-.8 2.5-.3l3.2 2.1c1 .7 1.1 2 .3 2.9l-1.4 1.6c-1 1.1-2.6 1.4-4 .8-6.2-2.5-10.5-7.3-12.3-13.4-.4-1.4 0-2.9 1.1-3.8z" fill="var(--white)"/>
        </svg>
        <span class="contact-text">518.677.3941</span>
      </li>
      <li class="contact-item">
        <svg class="contact-icon" viewBox="0 0 40 40" aria-hidden="true">
          <circle cx="20" cy="20" r="20" fill="var(--plum)"/>
          <g fill="none" stroke="var(--white)" stroke-width="1.5">
            <circle cx="20" cy="20" r="10"/>
            <ellipse cx="20" cy="20" rx="4.5" ry="10"/>
            <line x1="10" y1="20" x2="30" y2="20"/>
            <line x1="11.5" y1="15" x2="28.5" y2="15"/>
            <line x1="11.5" y1="25" x2="28.5" y2="25"/>
          </g>
        </svg>
        <span class="contact-text">calmbriefcounsel.net</span>
      </li>
      <li class="contact-item">
        <svg class="contact-icon" viewBox="0 0 40 40" aria-hidden="true">
          <circle cx="20" cy="20" r="20" fill="var(--plum)"/>
          <g fill="none" stroke="var(--white)" stroke-width="1.5" stroke-linejoin="round">
            <rect x="9.5" y="12.5" width="21" height="15" rx="1"/>
            <polyline points="9.5,13 20,21.5 30.5,13"/>
            <line x1="9.5" y1="27" x2="17" y2="19.5"/>
            <line x1="30.5" y1="27" x2="23" y2="19.5"/>
          </g>
        </svg>
        <span class="contact-text">marissa@calmbriefcounsel.net</span>
      </li>
      <li class="contact-item">
        <svg class="contact-icon" viewBox="0 0 40 40" aria-hidden="true">
          <circle cx="20" cy="20" r="20" fill="var(--plum)"/>
          <path d="M11 12.5h18a1.5 1.5 0 0 1 1.5 1.5v10a1.5 1.5 0 0 1-1.5 1.5H18l-5 4v-4h-2A1.5 1.5 0 0 1 9.5 24V14a1.5 1.5 0 0 1 1.5-1.5z" fill="none" stroke="var(--white)" stroke-width="1.5" stroke-linejoin="round"/>
          <circle cx="15" cy="19" r="1.3" fill="var(--white)"/>
          <circle cx="20" cy="19" r="1.3" fill="var(--white)"/>
          <circle cx="25" cy="19" r="1.3" fill="var(--white)"/>
        </svg>
        <span class="contact-text">@calmbriefcounsel</span>
      </li>
    </ul>
  </section>

</main>
</body>
</html>
```